High End Cosmetic Packaging Design Project

Looking for packaging for 2 products for a High end skin care line aimed at the 35+ year old women. Color scheme is Pantone 2765c with accents of metallic silver, copper or gold, Pantone colors 871-877c. Possible watermark in the background or a 3D image. We are open to any good ideas and suggestions. Box dimensions for the 2 products are small, approximately 4.375 inches high and 1.5 inches square. I have attached an image of the logo. I have the logo files in all the various forms. 1 box is for a Vitamin C Serum and the other box is for an Anti Aging Serum. Boxes are the same but the text will be different on both products. I will supply the text for the boxes later, including directions & ingredients and a UPC code that has to go on the underside of the box. It has to be an elegant design that will stand out in photos online. Good and quick communication & feedback between you and us is essential. I have attached a jpg of our new logo. I have this logo in all available forms
*****We are open to all ideas and want your ideas and input. The bottles that go inside these boxes are a deep violet almost black kovra glass. This is where the pantone color selection came from but upon further thought it may not be the right choice. We were out looking at cosmetic packaging today and thought also as an idea that a dark charcoal, or black box might work as well. We have seen boxes in those dark shades in glossy, matt and some with a sparkle finish. Embossed lettering may be a possibility as well. Copper letters may be an idea that works well also. These are just ideas rolling aroung in our heads but please give us your ideas*******
Reason: to give designers more time
This is for the 35+ year old woman.
Communication

```html
<!DOCTYPE html>
<html lang="en">
<head>
<meta charset="utf-8">
<title>Velmare Serum Carton Dieline</title>
<link rel="stylesheet" href="https://fonts.googleapis.com/css2?family=Josefin+Sans:wght@600&display=swap">
<style>
  :root {
    --paper: #ffffff;
    --cut-line: #3a3a3a;
    --band: #4db3f2;
    --wordmark: #1c1ca8;
    --aqua-deep: #a6dfee;
    --aqua-mid: #c6ebf5;
    --aqua-soft: #e2f5fa;
    --splash: #b3e3f2;
  }
  html, body {
    margin: 0;
    padding: 0;
    width: 1200px;
    height: 1000px;
    overflow: hidden;
    background: var(--paper);
  }
  .dieline {
    display: block;
    width: 1200px;
    height: 1000px;
  }
  .cut { fill: var(--paper); stroke: var(--cut-line); stroke-width: 1; }
  .fold { fill: none; stroke: var(--cut-line); stroke-width: 1; }
  .panel-edge { fill: none; stroke: var(--cut-line); stroke-width: 1; }
  .band { fill: var(--band); }
  .wordmark {
    font-family: "Josefin Sans", sans-serif;
    font-weight: 600;
    fill: var(--wordmark);
  }
  .stop-paper { stop-color: var(--paper); stop-opacity: 1; }
  .stop-aqua-deep { stop-color: var(--aqua-deep); stop-opacity: 1; }
  .stop-aqua-mid { stop-color: var(--aqua-mid); stop-opacity: 1; }
  .stop-aqua-soft { stop-color: var(--aqua-soft); stop-opacity: 1; }
  .stop-splash { stop-color: var(--splash); stop-opacity: 0.9; }
  .stop-splash-mid { stop-color: var(--splash); stop-opacity: 0.45; }
  .stop-splash-fade { stop-color: var(--splash); stop-opacity: 0; }
</style>
</head>
<body>
<svg class="dieline" viewBox="0 0 1200 1000" xmlns="http://www.w3.org/2000/svg">
  <defs>
    <linearGradient id="front-wash" x1="0" y1="0" x2="0" y2="1">
      <stop offset="0" class="stop-paper"/>
      <stop offset="0.42" class="stop-paper"/>
      <stop offset="0.7" class="stop-aqua-soft"/>
      <stop offset="1" class="stop-aqua-deep"/>
    </linearGradient>
    <linearGradient id="side-wash" x1="0" y1="0" x2="0" y2="1">
      <stop offset="0" class="stop-aqua-deep"/>
      <stop offset="0.22" class="stop-aqua-mid"/>
      <stop offset="0.45" class="stop-paper"/>
      <stop offset="0.62" class="stop-aqua-soft"/>
      <stop offset="1" class="stop-aqua-soft"/>
    </linearGradient>
    <linearGradient id="cap-wash" x1="0" y1="0" x2="0" y2="1">
      <stop offset="0" class="stop-paper"/>
      <stop offset="0.35" class="stop-paper"/>
      <stop offset="1" class="stop-aqua-deep"/>
    </linearGradient>
    <radialGradient id="splash-fill" cx="0.5" cy="0.5" r="0.5">
      <stop offset="0" class="stop-splash"/>
      <stop offset="0.55" class="stop-splash-mid"/>
      <stop offset="1" class="stop-splash-fade"/>
    </radialGradient>
  </defs>

  <!-- glue flap -->
  <polygon class="cut" points="222,270 186,298 186,757 222,789"/>

  <!-- top tuck flaps -->
  <polygon class="cut" points="400,270 400,245 415,238 428,195 576,195 576,270"/>
  <polygon class="cut" points="754,270 754,195 905,195 918,238 930,245 930,270"/>

  <!-- top closure cap -->
  <path class="cut" d="M576,270 L576,103 A89,103 0 0 1 754,103 L754,270 Z"/>
  <rect x="576" y="103" width="178" height="167" fill="url(#cap-wash)"/>
  <ellipse cx="618" cy="225" rx="50" ry="55" fill="url(#splash-fill)" role="img" aria-label="Soft water splash decoration"/>
  <line class="fold" x1="576" y1="103" x2="754" y2="103"/>
  <text class="wordmark" x="665" y="150" font-size="38" text-anchor="middle" textLength="150" lengthAdjust="spacingAndGlyphs">VELMARE</text>

  <!-- bottom flaps -->
  <polygon class="cut" points="222,789 222,965 400,963 400,868 550,868 562,818 576,805 576,789"/>
  <polygon class="cut" points="754,789 754,805 768,818 780,868 905,868 918,818 930,812 930,789"/>
  <polyline class="fold" points="576,789 576,805"/>

  <!-- main panels -->
  <rect x="222" y="287" width="178" height="486" fill="url(#front-wash)"/>
  <rect x="400" y="287" width="176" height="486" fill="url(#side-wash)"/>
  <rect x="576" y="287" width="178" height="486" fill="url(#front-wash)"/>
  <rect x="754" y="287" width="176" height="486" fill="url(#side-wash)"/>

  <!-- splash decoration areas -->
  <ellipse cx="340" cy="345" rx="60" ry="75" fill="url(#splash-fill)" role="img" aria-label="Water splash decoration, upper corner of front panel"/>
  <ellipse cx="275" cy="680" rx="65" ry="100" fill="url(#splash-fill)" role="img" aria-label="Water splash decoration, lower corner of front panel"/>
  <ellipse cx="690" cy="345" rx="60" ry="75" fill="url(#splash-fill)" role="img" aria-label="Water splash decoration, upper corner of back panel"/>
  <ellipse cx="630" cy="680" rx="65" ry="100" fill="url(#splash-fill)" role="img" aria-label="Water splash decoration, lower corner of back panel"/>

  <!-- panel outlines -->
  <rect class="panel-edge" x="222" y="287" width="178" height="486"/>
  <rect class="panel-edge" x="400" y="287" width="176" height="486"/>
  <rect class="panel-edge" x="576" y="287" width="178" height="486"/>
  <rect class="panel-edge" x="754" y="287" width="176" height="486"/>

  <!-- panel wordmarks -->
  <text class="wordmark" x="488" y="352" font-size="38" text-anchor="middle" textLength="152" lengthAdjust="spacingAndGlyphs">VELMARE</text>
  <text class="wordmark" x="842" y="350" font-size="38" text-anchor="middle" textLength="152" lengthAdjust="spacingAndGlyphs">VELMARE</text>
  <text class="wordmark" x="348" y="605" font-size="82" text-anchor="middle" dominant-baseline="central" textLength="310" lengthAdjust="spacingAndGlyphs" transform="rotate(90 348 605)">VELMARE</text>
  <text class="wordmark" x="702" y="605" font-size="82" text-anchor="middle" dominant-baseline="central" textLength="310" lengthAdjust="spacingAndGlyphs" transform="rotate(90 702 605)">VELMARE</text>

  <!-- colour bands -->
  <rect class="band" x="222" y="270" width="708" height="17"/>
  <rect class="band" x="222" y="773" width="708" height="16"/>
</svg>
</body>
</html>
```